依頼詳細
ジュエリー・アクセサリーサイトのバナー制作をお願い致します。ターゲットは20代女性としており、有名カメラマン・モデルを使用しています。
記載項目
サイト名:VO -vela o-
キャッチコピー:VELA ME BRAND NEW ME
サイズ
• 1020×550 pix
希望イメージ
シンプル 複雑
単色 カラフル
暗い 明るい
日常 高級
遊び心 厳粛
未来的 伝統的
女性的 男性的
希望する色
青系、茶系、グレー系
納品ファイル
• 高解像度JPG (.jpg)
• PNG形式 (.png)
補足説明
■ 選んだ理由

迅速なご対応をして頂き、誠に有難うございました。
また何かございましたら、よろしくお願い致します。

■ 提案者全員のお礼・コメント

この度はご応募して頂き、誠に有難うございました。
また何かございましたら、よろしくお願い致します。

```html
<!DOCTYPE html>
<html lang="en">
<head>
<meta charset="utf-8">
<title>VO -vela o- banners</title>
<link rel="stylesheet" href="https://fonts.googleapis.com/css2?family=Raleway:wght@300;400&display=swap">
<style>
  :root {
    --sky-bg: #dce8f3;
    --sky-fill: rgba(196, 216, 236, 0.85);
    --sky-line: #9fb8d2;
    --sky-copy: #a3bcd8;
    --rose-bg: #eadcd5;
    --rose-fill: rgba(220, 198, 186, 0.85);
    --rose-line: #b89e8e;
    --rose-copy: #a88a78;
    --cream-bg: #f8f4de;
    --cream-fill: rgba(240, 226, 186, 0.85);
    --cream-line: #cdb98a;
    --cream-copy: #cbb27c;
    --logo-ink: #3a3a3a;
  }
  * { margin: 0; padding: 0; box-sizing: border-box; }
  html, body { width: 742px; height: 1200px; overflow: hidden; background: #fff; }
  .canvas { position: relative; width: 742px; height: 1200px; font-family: "Raleway", sans-serif; }
  .banner { position: absolute; left: 0; width: 742px; overflow: hidden; }
  .banner--sky { top: 0; height: 395px; background: var(--sky-bg); }
  .banner--rose { top: 395px; height: 408px; background: var(--rose-bg); }
  .banner--cream { top: 803px; height: 397px; background: var(--cream-bg); }

  .photo { position: absolute; }
  .banner--sky .photo { left: 235px; top: 62px; width: 507px; height: 333px;
    background: linear-gradient(100deg, #e9edf0 0%, #d9dde0 30%, #a59d98 60%, #e6e2df 85%, #f2f0ee 100%); }
  .banner--rose .photo { left: 0; top: 60px; width: 480px; height: 340px;
    background: linear-gradient(100deg, #ddd0c0 0%, #c4aa90 35%, #8a7464 60%, #3f3835 80%, #5a504a 100%); }
  .banner--cream .photo { left: 235px; top: 47px; width: 507px; height: 350px;
    background: linear-gradient(160deg, #f5eedb 0%, #e9ddbd 45%, #d4bf8e 70%, #f1e8d0 100%); }

  .title-card { position: absolute; width: 235px; height: 218px; }
  .title-card__frame { position: absolute; inset: 0; border: 1.5px solid var(--line); }
  .title-card__fill { position: absolute; left: 10px; top: 10px; right: -10px; bottom: -10px; background: var(--fill); }
  .title-card__body { position: absolute; left: 18px; top: 30px; right: 0; }
  .banner--sky .title-card { left: 25px; top: 25px; --line: var(--sky-line); --fill: var(--sky-fill); --copy: var(--sky-copy); }
  .banner--rose .title-card { left: 478px; top: 28px; --line: var(--rose-line); --fill: var(--rose-fill); --copy: var(--rose-copy); }
  .banner--cream .title-card { left: 25px; top: 22px; --line: var(--cream-line); --fill: var(--cream-fill); --copy: var(--cream-copy); }

  .brand-name { font-size: 24px; font-weight: 400; color: var(--logo-ink); letter-spacing: 0.03em; white-space: nowrap; }
  .catch-copy { margin-top: 34px; font-size: 24px; font-weight: 400; line-height: 1.2; color: var(--copy); letter-spacing: 0.01em; white-space: nowrap; }
  .catch-copy span { display: block; }
</style>
</head>
<body>
<main class="canvas">
  <section class="banner banner--sky">
    <div class="photo" role="img" aria-label="Model with dark hair wearing a rectangular gold earring, in a white top"></div>
    <div class="title-card">
      <div class="title-card__fill"></div>
      <div class="title-card__frame"></div>
      <div class="title-card__body">
        <p class="brand-name">VO -vela o-</p>
        <p class="catch-copy"><span>VELA ME</span><span>BRAND NEW ME</span></p>
      </div>
    </div>
  </section>

  <section class="banner banner--rose">
    <div class="photo" role="img" aria-label="Model in a black jacket raising a hand to the forehead, wearing a gold bracelet"></div>
    <div class="title-card">
      <div class="title-card__fill"></div>
      <div class="title-card__frame"></div>
      <div class="title-card__body">
        <p class="brand-name">VO -vela o-</p>
        <p class="catch-copy"><span>VELA ME</span><span>BRAND NEW ME</span></p>
      </div>
    </div>
  </section>

  <section class="banner banner--cream">
    <div class="photo" role="img" aria-label="Gold bangle and two rectangular gold earrings lying in sunlight and shadow"></div>
    <div class="title-card">
      <div class="title-card__fill"></div>
      <div class="title-card__frame"></div>
      <div class="title-card__body">
        <p class="brand-name">VO -vela o-</p>
        <p class="catch-copy"><span>VELA ME</span><span>BRAND NEW ME</span></p>
      </div>
    </div>
  </section>
</main>
</body>
</html>
```